依頼詳細
開設告知を病院や行政、居宅介護支援事業所に行うための簡易的なチラシの作成をお願いいたします。情報量は最低限で、雰囲気重視、まずは時期と場所をしっかりと伝えて初期段階の営業を行うためのツールを想定しています。
記載項目
別紙資料をご確認ください。
サイズ
A4
ページ数
片面
希望イメージ
シンプル 複雑
単色 カラフル
暗い 明るい
日常 高級
遊び心 厳粛
未来的 伝統的
女性的 男性的
希望する色
納品ファイル
補足説明

スタッフの投票で決めました。

大変すばらしい提案をいただきましてありがとうございました。今後もパンフレット等、様々依頼をさせていただく予定ですので、今後とも宜しくお願い致します。

```html
<!DOCTYPE html>
<html lang="ja">
<head>
<meta charset="UTF-8">
<title>住宅型有料老人ホーム ひだまり 新規開設のお知らせ</title>
<link rel="stylesheet" href="https://fonts.googleapis.com/css2?family=M+PLUS+Rounded+1c:wght@500;700;800&family=Shippori+Mincho:wght@600;800&display=swap">
<style>
  :root{
    --paper:#f5efdf;
    --sky:#e3f1dc;
    --green:#3f9a4a;
    --green-deep:#2c7a38;
    --green-pale:#eaf5e1;
    --navy:#1f3f79;
    --orange:#e2572a;
    --yellow:#fff2a8;
    --white:#ffffff;
    --ink:#3a3a3a;
    --tree:#8cc66d;
    --tree-deep:#5ea44a;
    --people:#e9c9a8;
  }
  html,body{margin:0;padding:0;overflow:hidden;}
  body{width:853px;height:1200px;background:var(--paper);}
  .flyer{
    position:relative;width:853px;height:1200px;overflow:hidden;
    background:linear-gradient(180deg,var(--sky) 0,var(--sky) 560px,var(--paper) 760px);
    font-family:"M PLUS Rounded 1c",sans-serif;color:var(--ink);
  }
  .abs{position:absolute;}
  .art{position:absolute;border-radius:40px;}
  .art--trees{background:radial-gradient(circle at 50% 40%,var(--tree) 0,var(--tree-deep) 70%);}
  .art--people{background:linear-gradient(160deg,var(--people),#c9dcb8);}
  .art--stars{background:linear-gradient(90deg,#3c78c8,#7fb4e8,#3c78c8);border-radius:30px;opacity:.85;}

  .headline-arc{position:absolute;left:0;top:0;width:853px;height:120px;}
  .house{position:absolute;left:165px;top:80px;width:523px;height:630px;}

  .facility-type{top:196px;left:0;width:853px;text-align:center;font-size:30px;font-weight:800;color:var(--green-deep);letter-spacing:2px;white-space:nowrap;}
  .facility-name{top:226px;left:0;width:853px;text-align:center;font-family:"Shippori Mincho",serif;font-weight:800;font-size:78px;color:var(--navy);letter-spacing:6px;line-height:1.1;white-space:nowrap;}
  .facility-kanji{top:320px;left:0;width:853px;text-align:center;font-family:"Shippori Mincho",serif;font-weight:800;font-size:28px;color:var(--navy);letter-spacing:10px;}

  .opening{top:362px;left:212px;width:429px;height:158px;background:var(--green-pale);border:4px solid var(--green);border-radius:22px;text-align:center;box-sizing:border-box;overflow:hidden;}
  .opening__date{font-family:"Shippori Mincho",serif;font-weight:800;font-size:60px;color:var(--orange);line-height:1;margin-top:10px;letter-spacing:2px;white-space:nowrap;}
  .opening__word{font-family:"Shippori Mincho",serif;font-weight:800;font-size:72px;color:var(--orange);line-height:1.05;letter-spacing:6px;white-space:nowrap;}

  .badge-left{left:16px;top:200px;width:172px;box-sizing:border-box;padding:8px 4px;background:var(--yellow);border:3px solid var(--white);border-radius:16px;text-align:center;font-size:16px;font-weight:800;color:var(--navy);line-height:1.4;white-space:nowrap;}
  .badge-right{left:683px;top:262px;width:160px;text-align:center;}
  .badge-right__lead{box-sizing:border-box;background:var(--yellow);border:3px solid var(--white);border-radius:16px;font-size:16px;font-weight:800;color:var(--navy);line-height:1.4;padding:8px 4px;white-space:nowrap;}
  .badge-right__note{font-size:11px;color:var(--ink);line-height:1.4;margin-top:6px;white-space:nowrap;}

  .catch{top:536px;left:0;width:853px;text-align:center;font-size:31px;font-weight:800;color:var(--green-deep);letter-spacing:2px;white-space:nowrap;}
  .feature{top:590px;left:0;width:853px;text-align:center;font-size:27px;font-weight:800;color:var(--orange);line-height:1.35;white-space:nowrap;}

  .fees{top:675px;left:150px;width:553px;}
  .fees__tab{margin-left:auto;width:150px;background:var(--green);color:var(--white);font-weight:800;font-size:20px;text-align:center;border-radius:12px 12px 0 0;padding:3px 0;}
  .fees__rows{border-top:3px solid var(--green);border-bottom:3px solid var(--green);padding:8px 6px;font-size:20px;font-weight:700;color:var(--navy);white-space:nowrap;}
  .fees__total{display:flex;align-items:center;justify-content:space-between;margin-top:6px;}
  .fees__sum{font-size:38px;font-weight:800;color:var(--orange);}
  .fees__note{font-size:11px;color:var(--ink);width:170px;line-height:1.4;white-space:normal;}

  .contact{top:830px;left:30px;width:500px;background:var(--white);border-radius:18px;padding:14px 20px;box-sizing:border-box;}
  .contact__address{font-size:13px;line-height:1.5;}
  .contact__label{font-size:20px;font-weight:800;color:var(--green-deep);margin-top:6px;}
  .contact__phone{display:flex;align-items:center;gap:8px;font-size:46px;font-weight:800;color:var(--navy);line-height:1.1;white-space:nowrap;}
  .contact__operator{font-size:13px;line-height:1.5;}
  .map{top:830px;left:560px;width:262px;height:190px;background:var(--white);border:2px solid #cfc6b0;border-radius:12px;display:flex;align-items:center;justify-content:center;font-size:14px;color:#999;}
</style>
</head>
<body>
<main class="flyer">
  <svg class="headline-arc" viewBox="0 0 853 120" aria-label="若葉沼環境ふれあい公園徒歩1分。">
    <path id="arc" d="M70 105 Q426 -20 783 105" fill="none"/>
    <text font-family="M PLUS Rounded 1c, sans-serif" font-weight="800" font-size="40" fill="#3f9a4a" text-anchor="middle">
      <textPath href="#arc" startOffset="50%">若葉沼環境ふれあい公園徒歩1分。</textPath>
    </text>
  </svg>

  <div class="art art--trees" style="left:-30px;top:90px;width:200px;height:110px;" role="img" aria-label="木のイラスト"></div>
  <div class="art art--people" style="left:690px;top:100px;width:150px;height:150px;" role="img" aria-label="お年寄りとスタッフのイラスト"></div>
  <div class="art art--people" style="left:10px;top:330px;width:170px;height:240px;" role="img" aria-label="車椅子のお年寄りとスタッフのイラスト"></div>
  <div class="art art--trees" style="left:690px;top:420px;width:160px;height:210px;" role="img" aria-label="木のイラスト"></div>

  <svg class="house" viewBox="0 0 523 630" aria-hidden="true">
    <path d="M20 130 L261 10 L503 130 L503 600 Q503 620 483 620 L40 620 Q20 620 20 600 Z" fill="#ffffff"/>
  </svg>
  <div class="art art--stars" style="left:340px;top:115px;width:173px;height:70px;" role="img" aria-label="星のイラスト"></div>

  <div class="art" style="left:45px;top:135px;width:90px;height:58px;background:#7d8fa6;border-radius:10px;" role="img" aria-label="テレビのイラスト"></div>
  <div class="abs badge-left">シアタールーム等、<br>余暇設備が充実!</div>
  <div class="abs badge-right">
    <div class="badge-right__lead">畑・園芸スペース<br>もあります。</div>
    <div class="badge-right__note">季節の野菜や花を<br>入居者様と一緒に<br>育てることができます。</div>
  </div>

  <div class="abs facility-type">住宅型有料老人ホーム</div>
  <div class="abs facility-name">ひだまり</div>
  <div class="abs facility-kanji">陽溜</div>

  <div class="abs opening">
    <div class="opening__date">令和3年4月</div>
    <div class="opening__word">新規開設</div>
  </div>

  <div class="abs catch">自然豊かで落ち着いたホームです。</div>
  <div class="abs feature">理学療法士、作業療法士を配置し、<br>機能悪化防止、機能改善に力を入れています。</div>

  <section class="abs fees">
    <div class="fees__tab">費用</div>
    <div class="fees__rows">
      <div>○家賃：27,000円～ ○食費：39,000円 ○管理費：18,000円</div>
      <div class="fees__total">
        <span class="fees__sum">合計84,000円～</span>
        <span class="fees__note">※別途、介護保険の自己負担分がかかります。</span>
      </div>
    </div>
  </section>

  <section class="abs contact">
    <div class="contact__address">緑川県青葉市若葉町1234-5<br>若葉沼環境ふれあい公園まで徒歩1分のアクセス良好</div>
    <div class="contact__label">お問い合わせ先(開設準備室)</div>
    <div class="contact__phone">
      <svg width="40" height="40" viewBox="0 0 24 24" aria-hidden="true"><path fill="#1f3f79" d="M6.6 10.8a15.1 15.1 0 0 0 6.6 6.6l2.2-2.2a1 1 0 0 1 1-.25 11.4 11.4 0 0 0 3.6.57 1 1 0 0 1 1 1V20a1 1 0 0 1-1 1A17 17 0 0 1 3 4a1 1 0 0 1 1-1h3.5a1 1 0 0 1 1 1c0 1.25.2 2.45.57 3.6a1 1 0 0 1-.25 1z"/></svg>
      000-000-0000
    </div>
    <div class="contact__operator">併設施設：訪問介護事業所・通所介護事業所</div>
  </section>
  <div class="abs map" role="img" aria-label="周辺地図">MAP</div>

  <div class="art art--trees" style="left:-20px;top:1060px;width:260px;height:180px;" role="img" aria-label="木のイラスト"></div>
  <div class="art art--trees" style="left:620px;top:1050px;width:260px;height:190px;" role="img" aria-label="木のイラスト"></div>
</main>
</body>
</html>
```